Awesome photographers card for an awesome new business

Double sided business card Black background and silver logo in middle on one side. Details on otherside. please keep it simple

Photographer

Gavin Tolley
0482615073
GavinTolleyPhotography82@lumenpost.com
www.GavinTolleyPhotography.com.au
Instagram _Gavin_tolley

Requirements
Must have
• My logo in Silver
• please use instagram logo instead of "Instagram"

```html
<!DOCTYPE html>
<html lang="en">
<head>
<meta charset="utf-8">
<title>Gavin Tolley – Photographer Business Card</title>
<link rel="stylesheet" href="https://fonts.googleapis.com/css2?family=Kaushan+Script&family=Open+Sans:wght@400;600&display=swap">
<style>
  :root {
    --page: #ffffff;
    --card: #131313;
    --band: #282828;
    --silver: #c9c9c9;
    --silver-bright: #e6e6e6;
    --text: #dcdcdc;
    --ghost: rgba(255,255,255,0.09);
  }
  * { box-sizing: border-box; margin: 0; padding: 0; }
  html, body { width: 1200px; height: 1200px; overflow: hidden; background: var(--page); }
  body { position: relative; font-family: "Open Sans", Arial, sans-serif; color: var(--text); }

  .card {
    position: absolute; left: 153px; width: 900px; height: 540px;
    background: var(--card); overflow: hidden;
  }
  .card--front { top: 45px; }
  .card--back { top: 616px; }

  .band { position: absolute; left: 0; width: 100%; height: 34px; background: var(--band); }
  .band--upper { top: 399px; }
  .band--lower { top: 447px; }

  .brand-mark {
    position: absolute; border-radius: 50%;
    border: 5px solid var(--silver);
    display: flex; align-items: center; justify-content: center;
  }
  .brand-mark__name {
    font-family: "Open Sans", Arial, sans-serif; font-weight: 600;
    color: var(--silver); font-size: 34px; letter-spacing: 2px; white-space: nowrap;
  }
  .brand-mark--front { left: 79px; top: 67px; width: 320px; height: 320px; }
  .brand-mark--back { left: 309px; top: 70px; width: 320px; height: 320px; }
  .brand-mark--ghost { border-color: var(--ghost); }
  .brand-mark--ghost .brand-mark__name { color: var(--ghost); font-size: 42px; }
  .brand-mark--ghost-front { left: 531px; top: 223px; width: 380px; height: 380px; }
  .brand-mark--ghost-back { left: -41px; top: -112px; width: 400px; height: 400px; }

  .identity { position: absolute; left: 520px; top: 118px; width: 300px; text-align: center; }
  .identity__name {
    font-family: "Kaushan Script", cursive; font-size: 46px;
    color: var(--silver-bright); line-height: 1.1;
  }
  .identity__role { font-size: 19px; color: var(--text); margin-top: 2px; }

  .contact {
    position: absolute; display: flex; align-items: center;
    font-size: 17px; color: var(--text); height: 34px; white-space: nowrap;
  }
  .contact svg { width: 20px; height: 20px; margin-right: 12px; flex: none; }
  .contact--phone { left: 64px; top: 399px; }
  .contact--email { left: 64px; top: 447px; }
  .contact--web { left: 460px; top: 399px; }
  .contact--social { left: 460px; top: 447px; }

  .back-url {
    position: absolute; left: 0; top: 448px; width: 100%; height: 33px;
    display: flex; align-items: center; justify-content: center;
    font-size: 15px; color: var(--text);
  }
</style>
</head>
<body>

<section class="card card--front">
  <div class="brand-mark brand-mark--ghost brand-mark--ghost-front"><span class="brand-mark__name">Gavin Tolley</span></div>
  <div class="band band--upper"></div>
  <div class="band band--lower"></div>

  <div class="brand-mark brand-mark--front"><span class="brand-mark__name">Gavin Tolley</span></div>

  <div class="identity">
    <div class="identity__name">Gavin Tolley</div>
    <div class="identity__role">Photographer</div>
  </div>

  <div class="contact contact--phone">
    <svg viewBox="0 0 24 24" aria-hidden="true"><path fill="#dcdcdc" d="M6.6 10.8a15 15 0 0 0 6.6 6.6l2.2-2.2c.3-.3.7-.4 1-.2 1.1.4 2.3.6 3.6.6.6 0 1 .4 1 1V20c0 .6-.4 1-1 1A17 17 0 0 1 3 4c0-.6.4-1 1-1h3.5c.6 0 1 .4 1 1 0 1.3.2 2.5.6 3.6.1.3 0 .7-.2 1z"/></svg>
    0482615073
  </div>
  <div class="contact contact--email">
    <svg viewBox="0 0 24 24" aria-hidden="true"><rect x="2" y="5" width="20" height="14" fill="none" stroke="#dcdcdc" stroke-width="2"/><path d="M2 5l10 8 10-8" fill="none" stroke="#dcdcdc" stroke-width="2"/></svg>
    GavinTolleyPhotography82@lumenpost.com
  </div>
  <div class="contact contact--web">
    <svg viewBox="0 0 24 24" aria-hidden="true"><circle cx="12" cy="12" r="10" fill="#dcdcdc"/></svg>
    www.GavinTolleyPhotography.com.au
  </div>
  <div class="contact contact--social">
    <svg viewBox="0 0 24 24" aria-hidden="true"><rect x="3" y="3" width="18" height="18" fill="#dcdcdc"/></svg>
    _Gavin_tolley
  </div>
</section>

<section class="card card--back">
  <div class="brand-mark brand-mark--ghost brand-mark--ghost-back"><span class="brand-mark__name">Gavin Tolley</span></div>
  <div class="brand-mark brand-mark--back"><span class="brand-mark__name">Gavin Tolley</span></div>
  <div class="band band--upper"></div>
  <div class="band band--lower"></div>
  <div class="back-url">www.GavinTolleyPhotography.com.au</div>
</section>

</body>
</html>
```